Meadowlark Cleaning Services - Redesign

I've got my website designed a few years ago and it looks dated now. I would like to get a modern, happy, bright, and clean look. All the content needed can be found at my current website www.meadowlarkcs.example. Not necessarily need to use all of it, since I want something more clean and easy to read.
I need a 5 pages website:
HOME | SERVICES | ESTIMATE |TESTIMONIALS | CONTACT US

Industry/Entity Type

Janitorial Service

Number of Pages Required

5+ page

Colors
0792cd
34a6d7
85cae6
cee9f5
ebebeb
f0f0f0
f5f5f5
b1b1b1
000000

Requirements
Must have
• Who we are?
• Meadowlark Cleaning Services is a local, family-owned, client-focused house and office cleaning company that strives to ensure the highest level of customer satisfaction. We offer expert residential and commercial cleaning services to all the Seattle and Eastside areas.
• Why Meadowlark?
• √ We are insured, bonded and licensed.
•  Meadowlark Cleaning Service is Fully Insured so you can rest easy knowing your home is protected.
•  Copy of insurance available upon request.
•

√ We provide all supplies and equipments needed to thoroughly clean your home or business.

• √ We are not a franchise. We are a local, family-owned company.

• When you call Meadowlark Cleaning Services, you’ll always speak to one of the owners, which is a great benefit to you since this allows us to give you the personal attention and more time needed to clean your home the way you want it cleaned.

• √ We are good at what we do, and we like doing it.

```html
<!DOCTYPE html>
<html lang="en">
<head>
<meta charset="utf-8">
<title>Meadowlark Cleaning Services</title>
<link rel="stylesheet" href="https://fonts.googleapis.com/css2?family=Lato:ital,wght@0,400;0,700;0,900;1,400&family=Karla:wght@400;700&display=swap">
<style>
:root{
  --blue:#0792cd;
  --blue-mid:#34a6d7;
  --blue-soft:#5bbde8;
  --blue-pale:#cee9f5;
  --band:#ebf3fb;
  --grey-line:#ebebeb;
  --grey-bg:#f5f5f5;
  --grey-text:#8a8f98;
  --muted:#b1b1b1;
  --ink:#2a2a2a;
  --dark:#2b2b2b;
  --white:#ffffff;
}
*{box-sizing:border-box;margin:0;padding:0}
html,body{width:1200px;height:2233px;overflow:hidden}
body{font-family:"Karla",sans-serif;color:var(--ink);background:var(--white);position:relative}
.container{width:770px;margin:0 auto;position:relative}

/* header */
.site-header{height:72px;display:flex;align-items:center}
.site-header .container{display:flex;align-items:center;justify-content:space-between;width:780px}
.brand{display:flex;align-items:center;gap:8px;font-family:"Lato",sans-serif;font-weight:900;font-size:22px;color:var(--blue)}
.brand-mark{width:14px;height:14px;background:var(--blue);border-radius:50%}
.main-nav{display:flex;align-items:center;gap:26px;font-family:"Lato",sans-serif;font-size:9.5px;font-weight:700;letter-spacing:.4px}
.main-nav a{color:var(--ink);text-decoration:none}
.btn-quote{background:var(--blue);color:var(--white)!important;padding:11px 16px;margin-left:4px}

/* hero */
.hero{position:relative;height:490px;background:linear-gradient(180deg,#e9eef2 0%,#d4dbe2 45%,#a9b4c7 75%,#8791ad 100%)}
.hero-arrow{position:absolute;top:188px;width:34px;height:102px;background:var(--blue);display:flex;align-items:center;justify-content:center}
.hero-arrow.prev{left:0}.hero-arrow.next{right:0}
.hero-box{position:absolute;left:220px;top:264px;width:286px;height:226px;background:var(--blue)}
.hero-box h1{font-family:"Lato",sans-serif;font-weight:900;font-size:17px;line-height:23px;color:var(--white);padding:28px 28px 0}
.hero-box p{font-size:10.5px;line-height:16px;color:#d6edf8;padding:10px 28px 0}
.hero-call{position:absolute;left:0;bottom:0;width:100%;height:56px;background:#0583bb;display:flex;align-items:center;padding:0 24px;gap:10px}
.hero-call small{font-family:"Lato",sans-serif;font-weight:700;font-size:7.5px;line-height:9px;color:var(--white);padding-right:12px;border-right:1px solid rgba(255,255,255,.4)}
.hero-call strong{font-family:"Lato",sans-serif;font-size:21px;color:var(--white);font-weight:700}

/* section heads */
.eyebrow{font-family:"Lato",sans-serif;font-size:9px;color:#555;text-transform:uppercase;letter-spacing:.3px}
.title{font-family:"Lato",sans-serif;font-weight:900;font-size:18px;color:#2e3440;margin-top:4px}
.rule{width:52px;height:1px;background:var(--blue-mid);margin-top:10px}
.centered{text-align:center}.centered .rule{margin:10px auto 0}

/* why */
.why{height:467px;padding-top:49px;position:relative}
.why-grid{display:grid;grid-template-columns:repeat(3,1fr);width:770px;margin:30px auto 0}
.why-item{height:154px;text-align:center;padding-top:3px}
.why-item:nth-child(-n+3){border-bottom:1px dashed #dcdcdc}
.why-item:nth-child(3n+2){border-left:1px dashed #dcdcdc;border-right:1px dashed #dcdcdc}
.why-item:nth-child(n+4){padding-top:14px}
.tick{width:67px;height:67px;border-radius:50%;background:var(--dark);margin:0 auto;display:flex;align-items:center;justify-content:center}
.tick.active{background:var(--blue)}
.why-item p{font-size:10.5px;line-height:16px;color:#444;margin:22px auto 0;width:210px}
.why-chevron{position:absolute;top:250px}

/* about + services */
.about{height:454px;background:var(--band);padding-top:65px}
.about .container{display:flex;justify-content:space-between}
.about-col{width:380px}
.services-col{width:369px}
.about-photo{width:380px;height:151px;margin-top:42px;background:linear-gradient(135deg,#dcd6cc 0%,#c9c6b8 40%,#8fa04c 70%,#e8e4dc 100%)}
.about-col p{font-size:10.5px;line-height:16px;color:var(--grey-text);margin-top:18px}
.accordion{margin-top:42px}
.acc-item{height:32px;background:var(--white);display:flex;align-items:center;justify-content:space-between;padding:0 20px;font-family:"Lato",sans-serif;font-weight:700;font-size:8.5px;color:#333;margin-bottom:1px;letter-spacing:.3px}
.acc-item span{color:var(--blue);font-size:13px}
.acc-item.open{background:var(--blue);color:var(--white)}
.acc-item.open span{color:var(--white)}
.acc-body{background:var(--band);padding:18px 22px 20px;height:116px}
.acc-body h3{font-family:"Lato",sans-serif;font-weight:700;font-size:12.5px;line-height:17px;color:#333}
.acc-body p{font-size:10px;line-height:15px;color:var(--grey-text);margin-top:8px}

/* testimonials */
.testimonials{height:380px;padding-top:45px}
.cards{display:flex;gap:33px;width:758px;margin:34px auto 0}
.card{width:231px}
.quote{position:relative;height:149px;background:var(--blue-soft);padding:24px 22px;font-family:"Lato",sans-serif;font-style:italic;font-size:10.5px;line-height:19px;color:var(--white)}
.quote::after{content:"";position:absolute;left:26px;bottom:-9px;border-left:10px solid var(--blue-soft);border-bottom:9px solid transparent}
.author{display:flex;align-items:center;gap:13px;margin-top:24px}
.avatar{width:27px;height:27px;border-radius:50%;background:linear-gradient(135deg,#c9a58a,#5a6b8a)}
.author b{display:block;font-family:"Lato",sans-serif;font-size:9px;font-weight:700;color:#333}
.author i{font-family:"Lato",sans-serif;font-size:8.5px;color:var(--grey-text)}

/* cta */
.cta{height:90px;background:var(--dark)}
.cta .container{height:90px;display:flex;align-items:center;justify-content:space-between;width:760px}
.cta h2{font-family:"Lato",sans-serif;font-weight:900;font-size:14px;color:var(--white)}
.cta p{font-family:"Lato",sans-serif;font-style:italic;font-size:10px;color:#ddd;margin-top:5px}
.btn-light{background:var(--white);color:#222;font-family:"Lato",sans-serif;font-weight:700;font-size:8.5px;padding:9px 35px;letter-spacing:.3px}

/* footer */
.site-footer{height:280px;padding-top:56px}
.site-footer .container{width:760px;display:flex}
.foot-head{font-family:"Lato",sans-serif;font-size:11px;color:#333;margin-bottom:20px}
.foot-menu{width:394px}
.menu-cols{display:flex}
.menu-cols ul{list-style:none;font-family:"Lato",sans-serif;font-size:8.5px;color:var(--grey-text);letter-spacing:.3px}
.menu-cols ul li{height:24px}
.menu-cols ul+ul{border-left:1px solid var(--grey-line);padding-left:14px}
.menu-cols ul:nth-child(1){width:95px}.menu-cols ul:nth-child(2){width:100px}
.menu-cols li.current{color:#222}
.foot-contact{width:260px;font-size:9.5px;color:var(--grey-text)}
.c-row{display:flex;gap:10px;margin-bottom:18px;line-height:15px}
.pay{margin-top:40px;text-align:center;font-size:8.5px;color:#555}
.badge{width:60px;height:60px;border-radius:50%;background:radial-gradient(circle,#f5c531,#d59a10);margin:0 auto 16px}
.pay-cards{display:flex;gap:4px;margin-top:8px}
.pay-cards span{width:24px;height:15px;border:1px solid #ddd;background:var(--grey-bg)}
.foot-bottom{position:absolute;left:220px;right:218px;top:2177px;display:flex;justify-content:space-between;align-items:center}
.social{display:flex;gap:11px}
.social span{width:11px;height:11px;background:#6e7fa1;border-radius:2px}
.copyright{font-family:"Lato",sans-serif;font-size:8.5px;color:#444;letter-spacing:.2px}
</style>
</head>
<body>

<header class="site-header">
  <div class="container">
    <div class="brand"><span class="brand-mark"></span>Meadowlark</div>
    <nav class="main-nav">
      <a href="#">HOME</a><a href="#">SERVICES</a><a href="#">ESTIMATE</a><a href="#">TESTIMONIALS</a><a href="#">CONTACT US</a>
      <a href="#" class="btn-quote">REQUEST FOR QUOTE</a>
    </nav>
  </div>
</header>

<section class="hero" role="img" aria-label="Photo of a bright, clean open-plan office with cubicles and blue chairs">
  <div class="hero-arrow prev"><svg width="10" height="14" viewBox="0 0 10 14"><path d="M8 1 2 7l6 6" fill="none" stroke="#fff" stroke-width="2.4"/></svg></div>
  <div class="hero-arrow next"><svg width="10" height="14" viewBox="0 0 10 14"><path d="M2 1l6 6-6 6" fill="none" stroke="#fff" stroke-width="2.4"/></svg></div>
  <div class="hero-box">
    <h1>WELCOME TO MEADOWLARK CLEANING SERVICES</h1>
    <p>Lorem ipsum dolor sit amet, consectetur adipis cing elit. Etiam sed augue vitae ex vulputate venenatis.</p>
    <div class="hero-call">
      <svg width="16" height="16" viewBox="0 0 16 16"><rect width="16" height="16" rx="3" fill="#fff"/><path d="M5 3.5c-.8.4-1.4 1.3-1 2.6 1 3 3 5 5.9 5.9 1.3.4 2.2-.2 2.6-1l-1.9-1.6-1.3.9c-1.2-.6-2.2-1.6-2.7-2.7l.9-1.3z" fill="#0583bb"/></svg>
      <small>BOOK THROUGH<br>CALL NOW</small>
      <strong>555-013-2468</strong>
    </div>
  </div>
</section>

<section class="why">
  <div class="centered">
    <div class="eyebrow">Amet, consectetur</div>
    <h2 class="title">WHY MEADOWLARK?</h2>
    <div class="rule"></div>
  </div>
  <svg class="why-chevron" style="left:143px" width="26" height="52" viewBox="0 0 26 52"><path d="M24 1 2 26l22 25" fill="none" stroke="#e4e4e4" stroke-width="1.5"/></svg>
  <svg class="why-chevron" style="left:1030px" width="26" height="52" viewBox="0 0 26 52"><path d="M2 1l22 25L2 51" fill="none" stroke="#e4e4e4" stroke-width="1.5"/></svg>
  <div class="why-grid">
    <div class="why-item"><div class="tick active"><svg width="18" height="14" viewBox="0 0 18 14"><path d="M2 7l5 5 9-10" fill="none" stroke="#fff" stroke-width="3"/></svg></div><p>We are insured, bonded and licensed</p></div>
    <div class="why-item"><div class="tick"><svg width="18" height="14" viewBox="0 0 18 14"><path d="M2 7l5 5 9-10" fill="none" stroke="#fff" stroke-width="3"/></svg></div><p>Meadowlark Cleaning Service is Fully Insured so you can rest easy knowing your home is protected.</p></div>
    <div class="why-item"><div class="tick"><svg width="18" height="14" viewBox="0 0 18 14"><path d="M2 7l5 5 9-10" fill="none" stroke="#fff" stroke-width="3"/></svg></div><p>Copy of insurance available upon request.</p></div>
    <div class="why-item"><div class="tick"><svg width="18" height="14" viewBox="0 0 18 14"><path d="M2 7l5 5 9-10" fill="none" stroke="#fff" stroke-width="3"/></svg></div><p>We provide all supplies and equipments needed to thoroughly clean your home or business.</p></div>
    <div class="why-item"><div class="tick"><svg width="18" height="14" viewBox="0 0 18 14"><path d="M2 7l5 5 9-10" fill="none" stroke="#fff" stroke-width="3"/></svg></div><p>are not a franchise. We are a local, family-owned company.</p></div>
    <div class="why-item"><div class="tick"><svg width="18" height="14" viewBox="0 0 18 14"><path d="M2 7l5 5 9-10" fill="none" stroke="#fff" stroke-width="3"/></svg></div><p>We are good at what we do, and we like doing it.</p></div>
  </div>
</section>

<section class="about">
  <div class="container">
    <div class="about-col">
      <div class="eyebrow">Lorem ipsum dolor sit</div>
      <h2 class="title">WHO WE ARE?</h2>
      <div class="rule"></div>
      <div class="about-photo" role="img" aria-label="Photo of cleaners tidying a bright living room"></div>
      <p>Meadowlark Cleaning Services is a local, family-owned, client-focused house and office cleaning company that strives to ensure the highest level of customer satisfaction. We offer expert residential and commercial cleaning services to all the Seattle and Eastside areas.</p>
    </div>
    <div class="services-col">
      <div class="eyebrow">Variety of services</div>
      <h2 class="title">OUR SERVICES</h2>
      <div class="rule"></div>
      <div class="accordion">
        <div class="acc-item">OFFICE CLEANING <span>+</span></div>
        <div class="acc-item open">RESIDENTIAL CLEANING <span>&minus;</span></div>
        <div class="acc-body">
          <h3>LOREM IPSUM DOLOR SIT AMET, CONSECTETURINH THE ADIPISCING ELIT.</h3>
          <p>Fusce ut velit semper, semper arcu quis, aliquam magna. Etiam sed justo et sem varius euismod. In ac justo urna. Donec tincid unt nisl semper sapien ullamcorper,</p>
        </div>
        <div class="acc-item">MOVE OUT/IN CLEANING <span>+</span></div>
        <div class="acc-item">SCHOOL/DAYCARE CLEANING <span>+</span></div>
      </div>
    </div>
  </div>
</section>

<section class="testimonials">
  <div class="centered">
    <div class="eyebrow">What people say</div>
    <h2 class="title">OUR TESTIMONIALS</h2>
    <div class="rule"></div>
  </div>
  <div class="cards">
    <div class="card">
      <div class="quote">Etiam tristique sagittis pulvinar. Cras scelerisque dui ut, bibendum ante, dit neque eget lobortis. Nam eleifend sollicitudin nulla quis Interdum et malesuada fames.</div>
      <div class="author"><div class="avatar" role="img" aria-label="Client portrait"></div><div><b>MARCUS ELLERY</b><i>www.brightpage.example</i></div></div>
    </div>
    <div class="card">
      <div class="quote">Etiam tristique sagittis pulvinar. Cras scelerisque dui ut, bibendum ante, dit neque eget lobortis. Nam eleifend sollicitudin nulla quis Interdum et malesuada fames.</div>
      <div class="author"><div class="avatar" role="img" aria-label="Client portrait"></div><div><b>PRIYA HALVORSEN</b><i>www.hollowtree.example</i></div></div>
    </div>
    <div class="card">
      <div class="quote">Etiam tristique sagittis pulvinar. Cras scelerisque dui ut, bibendum ante, dit neque eget lobortis. Nam eleifend sollicitudin nulla quis Interdum et malesuada fames.</div>
      <div class="author"><div class="avatar" role="img" aria-label="Client portrait"></div><div><b>TESSA MONROE</b><i>www.brightpage.example</i></div></div>
    </div>
  </div>
</section>

<section class="cta">
  <div class="container">
    <div>
      <h2>WANT OUR SERVICE?</h2>
      <p>Lorem ipsum dolor sit amet, consectetur adipiscing elit. Pellentesque lacinia, ipsum eu vulputate pulvinar,</p>
    </div>
    <a class="btn-light">CONTACT US NOW</a>
  </div>
</section>

<footer class="site-footer">
  <div class="container">
    <div class="foot-menu">
      <div class="foot-head">MENU</div>
      <div class="menu-cols">
        <ul><li class="current">HOME</li><li>SERVICES</li><li>LOREM IPSUM</li><li>DEPARTMENT</li><li>PAGES</li></ul>
        <ul><li>BLOG</li><li>CONTACT</li><li>SHOP</li><li>FAQ</li><li>CONTATNRY</li></ul>
        <ul><li>TERMS &amp; CONDITION</li><li>PRIVACY POLICY</li><li>LEGAL DESCLAIMER</li><li>SITEMAP</li></ul>
      </div>
    </div>
    <div class="foot-contact">
      <div class="foot-head">CONTACT</div>
      <div class="c-row"><svg width="8" height="11" viewBox="0 0 8 11"><path d="M4 0a4 4 0 0 0-4 4c0 3 4 7 4 7s4-4 4-7a4 4 0 0 0-4-4z" fill="#8a8f98"/><circle cx="4" cy="4" r="1.4" fill="#fff"/></svg><span>Suite 12, Cedar Lane,<br>USA 000000</span></div>
      <div class="c-row"><svg width="10" height="8" viewBox="0 0 10 8"><rect x=".5" y=".5" width="9" height="7" fill="none" stroke="#8a8f98"/><path d="M.5.5 5 4.5 9.5.5" fill="none" stroke="#8a8f98"/></svg><span>Email- info@meadowlarkcs.example</span></div>
      <div class="c-row"><svg width="9" height="9" viewBox="0 0 16 16"><path d="M4 1C2.5 1.6 1.2 3.3 2 5.8c1.6 4.4 4 6.8 8.2 8.2 2.5.8 4.2-.5 4.8-2l-3-2.6-2 1.4c-1.8-.9-3.3-2.4-4.1-4.1l1.4-2z" fill="#8a8f98"/></svg><span>555-013-2468</span></div>
    </div>
    <div class="pay">
      <div class="badge" role="img" aria-label="Satisfaction guarantee seal"></div>
      Payment Center
      <div class="pay-cards"><span></span><span></span><span></span><span></span></div>
    </div>
  </div>
</footer>
<div class="foot-bottom">
  <div class="social"><span></span><span></span><span></span><span></span><span></span><span></span></div>
  <div class="copyright">© 2016 ALL RIGHTS RESERVED MEADOWLARK CLEANING SERVICES</div>
</div>

</body>
</html>
```